Briefpapier und Visitenkarten
Zielgruppe
In erster Linie mir selbst.
Aufgabenstellung
Gestaltung von Visitenkarten und Briefpapier.
Visitenkarten: Gestaltung beidseitig und in Pantone Farben
Briefpapier: Gestaltung einseitig und in Pantone Farben
Briefpapier und Visitenkarten sollen ein Design haben.

```html
<!DOCTYPE html>
<html lang="de">
<head>
<meta charset="utf-8">
<title>Kolthaus Werbeagentur – Geschäftsausstattung</title>
<link rel="stylesheet" href="https://fonts.googleapis.com/css2?family=Didact+Gothic&display=swap">
<style>
  :root {
    --stage: #2e2e30;
    --paper: #ffffff;
    --card-grey: #babbbe;
    --ink: #8c8c90;
    --ink-dark: #6f6f74;
    --ink-light: #a9a9ad;
    --mark-faint: #ededee;
    --logo-light: #e6e6e8;
  }
  * { margin: 0; padding: 0; box-sizing: border-box; }
  html, body { width: 1200px; height: 1200px; overflow: hidden; }
  body {
    background: var(--stage);
    font-family: "Didact Gothic", "Century Gothic", sans-serif;
    color: var(--ink);
    position: relative;
  }
  .sheet { position: absolute; }

  /* logo lockup */
  .lockup { display: flex; flex-direction: column; align-items: center; color: var(--ink); }
  .lockup-dot { border-radius: 50%; background: currentColor; }
  .lockup-name { letter-spacing: 0.02em; white-space: nowrap; line-height: 1; }
  .lockup-claim { letter-spacing: 0.12em; white-space: nowrap; line-height: 1; }

  /* business card front */
  .card-front {
    left: 62px; top: 254px; width: 493px; height: 326px;
    background: var(--paper);
    display: flex; align-items: center; justify-content: center;
  }
  .card-front .lockup-dot { width: 52px; height: 52px; margin-bottom: 10px; }
  .card-front .lockup-name { font-size: 24px; }
  .card-front .lockup-claim { font-size: 10px; margin-top: 7px; }

  /* business card back */
  .card-back {
    left: 62px; top: 597px; width: 493px; height: 325px;
    background: var(--card-grey);
    color: var(--ink-dark);
  }
  .card-back .side-logo {
    position: absolute; left: 24px; top: 30px; bottom: 30px; width: 130px;
  }
  .card-back .side-dot {
    position: absolute; left: 4px; top: 128px;
    width: 44px; height: 44px; border-radius: 50%; background: var(--ink-dark);
  }
  .card-back .side-text {
    position: absolute; left: 96px; top: 0;
    transform-origin: top left; transform: rotate(90deg);
    display: flex; flex-direction: column; align-items: center;
  }
  .card-back .side-text .lockup-name { font-size: 22px; }
  .card-back .side-text .lockup-claim { font-size: 9px; margin-top: 6px; }
  .holder { position: absolute; right: 40px; top: 70px; text-align: right; }
  .holder-name { font-size: 24px; line-height: 1.1; }
  .holder-role { font-size: 12px; color: var(--ink-dark); }
  .contact { position: absolute; right: 40px; top: 182px; text-align: right; font-size: 11px; line-height: 1.9; }
  .contact .sep { padding: 0 8px; }

  /* letterhead */
  .letterhead {
    left: 573px; top: 254px; width: 521px; height: 843px;
    background: var(--paper);
  }
  .letterhead .head { position: absolute; left: 0; right: 0; top: 36px; }
  .letterhead .head .lockup-dot { width: 40px; height: 40px; margin-bottom: 7px; }
  .letterhead .head .lockup-name { font-size: 18px; }
  .letterhead .head .lockup-claim { font-size: 8px; margin-top: 5px; }
  .faint-mark {
    position: absolute; left: 216px; top: 555px;
    width: 140px; height: 140px; border-radius: 50%; background: var(--mark-faint);
  }
  .letterhead .foot { position: absolute; left: 0; right: 0; top: 738px; text-align: center; }
  .foot-name { font-size: 12px; line-height: 1.1; }
  .foot-role { font-size: 8px; color: var(--ink-light); }
  .foot-brand { font-size: 16px; margin-top: 6px; letter-spacing: 0.02em; }
  .foot-rule { width: 230px; height: 1px; background: var(--mark-faint); margin: 8px auto 6px; }
  .foot-line { font-size: 6.5px; line-height: 1.7; color: var(--ink-light); }

  /* logo presentation on dark */
  .logo-show { left: 62px; top: 985px; width: 430px; color: var(--logo-light); }
  .logo-show .lockup-dot { width: 66px; height: 66px; margin-bottom: 12px; }
  .logo-show .lockup-name { font-size: 29px; }
  .logo-show .lockup-claim { font-size: 11px; margin-top: 8px; }
</style>
</head>
<body>

  <section class="sheet card-front" aria-label="Visitenkarte Vorderseite">
    <div class="lockup">
      <span class="lockup-dot"></span>
      <span class="lockup-name">KOLTHAUS WERBEAGENTUR</span>
      <span class="lockup-claim">Ideen, die wachsen</span>
    </div>
  </section>

  <section class="sheet card-back" aria-label="Visitenkarte Rückseite">
    <div class="side-logo">
      <span class="side-dot"></span>
      <div class="side-text">
        <span class="lockup-name">KOLTHAUS WERBEAGENTUR</span>
        <span class="lockup-claim">Ideen, die wachsen</span>
      </div>
    </div>
    <div class="holder">
      <p class="holder-name">Jonas Kolthaus</p>
      <p class="holder-role">[Inhaber]</p>
    </div>
    <div class="contact">
      <p>Büro:</p>
      <p>Ahornweg 12<span class="sep">|</span>D-50999 Feldberg</p>
      <p>www.kolthauswa.de<span class="sep">|</span>info@kolthauswa.de</p>
    </div>
  </section>

  <section class="sheet letterhead" aria-label="Briefpapier">
    <div class="head lockup">
      <span class="lockup-dot"></span>
      <span class="lockup-name">KOLTHAUS WERBEAGENTUR</span>
      <span class="lockup-claim">Ideen, die wachsen</span>
    </div>
    <span class="faint-mark"></span>
    <div class="foot">
      <p class="foot-name">Jonas Kolthaus</p>
      <p class="foot-role">[Inhaber]</p>
      <p class="foot-brand">KOLTHAUS WERBEAGENTUR</p>
      <div class="foot-rule"></div>
      <p class="foot-line">www.kolthauswa.de | info@kolthauswa.de</p>
      <p class="foot-line">Bankverbindung: Stadtbank Feldberg | BLZ 380 500 00 | Konto 1234567</p>
    </div>
  </section>

  <section class="sheet logo-show lockup" aria-label="Logo">
    <span class="lockup-dot"></span>
    <span class="lockup-name">KOLTHAUS WERBEAGENTUR</span>
    <span class="lockup-claim">Ideen, die wachsen</span>
  </section>

</body>
</html>
```